Tallbrook Sonic Group, Inc.
Project: Business Cards
Business Cards  - Health
Business Cards
Professional
2 Versions: Person 1. Marla Pennington, BSBA, BSDMS, RDMS Person 2. Gavin Pennington
Person 1. [no title] Person 2. Vice President, Sales
Ultrasound Services Sonographer Staffing PACS / Reporting
info@tallbrooksg.com
www.tallbrooksg.com
Member: CVRTB, NLUA & PSEK
Would prefer light color(s) or white background to match logo - no black backgrounds please. Let me know if you have any questions. Thanks!

```html
<!DOCTYPE html>
<html lang="en">
<head>
<meta charset="utf-8">
<title>Tallbrook Sonic Group, Inc. — Business Cards</title>
<link href="https://fonts.googleapis.com/css2?family=Lato:wght@400;700&display=swap" rel="stylesheet">
<style>
  :root {
    --stage: #e6e8ea;
    --card: #ffffff;
    --teal: #1d4d5c;
    --teal-dark: #163c48;
    --slate: #5a6e78;
    --ink: #2b3a42;
    --muted: #6b7780;
    --band-grey: #c9cfd3;
  }
  * { margin: 0; padding: 0; box-sizing: border-box; }
  html, body { width: 1200px; height: 901px; overflow: hidden; }
  body {
    background: var(--stage);
    font-family: "Lato", sans-serif;
    position: relative;
  }
  .card {
    position: absolute;
    width: 516px;
    height: 310px;
    background: var(--card);
    box-shadow: 0 4px 14px rgba(0,0,0,.18);
    overflow: hidden;
  }
  .card--back { left: 316px; top: 75px; width: 538px; }
  .card--front-a { left: 61px; top: 445px; }
  .card--front-b { left: 635px; top: 445px; }

  .brand {
    display: flex;
    align-items: center;
    gap: 10px;
    color: var(--slate);
    font-weight: 400;
    letter-spacing: .5px;
    white-space: nowrap;
  }
  .brand__dot {
    width: 22px; height: 22px; border-radius: 50%;
    background: var(--slate); flex: none;
  }
  .card--back .brand {
    position: absolute; left: 0; right: 0; top: 138px;
    justify-content: center; font-size: 20px;
  }
  .card .brand--front {
    position: absolute; left: 24px; top: 32px; font-size: 21px;
  }

  .person {
    position: absolute; right: 30px; top: 128px; text-align: right;
    color: var(--ink);
  }
  .person__name { font-size: 17px; font-weight: 700; color: var(--teal-dark); }
  .person__role { font-size: 12px; margin-top: 5px; letter-spacing: .3px; }

  .membership {
    position: absolute; right: 30px; top: 244px;
    font-size: 10.5px; line-height: 15px; color: var(--muted);
    white-space: nowrap;
  }

  .services {
    position: absolute; left: 24px; top: 187px;
    list-style: none; font-size: 10.5px; line-height: 15px; color: var(--muted);
  }
  .contact {
    position: absolute; left: 24px; top: 240px;
    list-style: none; font-size: 10.5px; line-height: 15px; color: var(--muted);
  }
  .contact li { display: flex; align-items: center; gap: 6px; }
  .contact svg { width: 10px; height: 10px; fill: var(--teal); }

  .band { position: absolute; left: 0; bottom: 0; width: 516px; height: 36px; }
  .band__url {
    position: absolute; right: 28px; bottom: 11px;
    color: #fff; font-size: 11px; letter-spacing: 2px;
  }
</style>
</head>
<body>

  <section class="card card--back" aria-label="Card back">
    <div class="brand"><span class="brand__dot"></span>Tallbrook Sonic Group, Inc.</div>
  </section>

  <section class="card card--front-a" aria-label="Card front, Marla Pennington">
    <div class="brand brand--front"><span class="brand__dot"></span>Tallbrook Sonic Group, Inc.</div>
    <div class="person">
      <p class="person__name">Marla Pennington</p>
      <p class="person__role">BSBA, &nbsp;BSDMS, &nbsp;RDMS</p>
    </div>
    <ul class="services">
      <li>Ultrasound Services</li>
      <li>Sonographer Staffing</li>
      <li>PACS / Reporting</li>
    </ul>
    <ul class="contact">
      <li><svg viewBox="0 0 10 10"><path d="M2 0h2l1 3-1.5 1a6 6 0 0 0 2.5 2.5L7 5l3 1v2a2 2 0 0 1-2 2A8 8 0 0 1 0 2a2 2 0 0 1 2-2z"/></svg>(555) 014-2124</li>
      <li><svg viewBox="0 0 10 10"><path d="M0 2h10v6H0z"/></svg>info@tallbrooksg.com</li>
    </ul>
    <p class="membership">Member: CVRTB, NLUA &amp; PSEK</p>
    <svg class="band" viewBox="0 0 516 36" preserveAspectRatio="none">
      <polygon points="196,0 516,0 516,36 180,36" fill="var(--band-grey)"/>
      <polygon points="222,0 516,0 516,36 206,36" fill="var(--teal)"/>
    </svg>
    <span class="band__url">www.tallbrooksg.com</span>
  </section>

  <section class="card card--front-b" aria-label="Card front, Gavin Pennington">
    <div class="brand brand--front"><span class="brand__dot"></span>Tallbrook Sonic Group, Inc.</div>
    <div class="person">
      <p class="person__name">Gavin Pennington</p>
      <p class="person__role">Vice President, Sales</p>
    </div>
    <ul class="services">
      <li>Ultrasound Services</li>
      <li>Sonographer Staffing</li>
      <li>PACS / Reporting</li>
    </ul>
    <ul class="contact">
      <li><svg viewBox="0 0 10 10"><path d="M2 0h2l1 3-1.5 1a6 6 0 0 0 2.5 2.5L7 5l3 1v2a2 2 0 0 1-2 2A8 8 0 0 1 0 2a2 2 0 0 1 2-2z"/></svg>(555) 014-2124</li>
      <li><svg viewBox="0 0 10 10"><path d="M0 2h10v6H0z"/></svg>info@tallbrooksg.com</li>
    </ul>
    <p class="membership">Member: CVRTB, NLUA &amp; PSEK</p>
    <svg class="band" viewBox="0 0 516 36" preserveAspectRatio="none">
      <polygon points="196,0 516,0 516,36 180,36" fill="var(--band-grey)"/>
      <polygon points="222,0 516,0 516,36 206,36" fill="var(--teal)"/>
    </svg>
    <span class="band__url">www.tallbrooksg.com</span>
  </section>

</body>
</html>
```